Etiketten für Saft-Range
grupotrinka suchte ein neues Design in der Kategorie Etiketten und hat ein Projekt auf grafikwerkstube.de gestartet.
Zielgruppe
Wir sind Getränkehersteller- und -händler. Für unsere Partner haben wir exklusive Eigenmarken, die nur unserer Partner verkaufen. Die veski Saft-Range ist eine exklusive Gastronomiemarke, die nicht im Handel erhältlich ist.
Aufgabenstellung
Das Layout unsere Eigenmarke veski soll in der Saft-Range einen Relaunch erhalten. Das ganze Sortiment besteht aktuell aus 10 Sorten. Es handelt sich um Glasflaschenetiketten, neue Stanzen beigefügt (Frontbauchetikett, Fronthalsetikett, Rückseitenetikett). Im ersten Schritt möchten wir nur die Sorten Kirsche & Apfel naturtrüb designen lassen.
Die Stanzen finden Sie beigefügt, sowie die aktuellen Layouts und Produktabbildungen der beiden genannten Sorten.
Zur Info, unsere Marke veski besteht ebenfalls aus einer Wasser-Range und Bittergetränke-Range. Die Abbildungen finden Sie zur Info ebenfalls anbei.
Folgende Bestandteile müssen auf die Etiketten (Materialfarbe weiß):
Front Bauchetikett:
- ob die Frucht als Foto oder als Zeichnung abgebildet wird ist uns erst einmal
- Marke veski
- Sorte
- Sortenzusatz wie z.B. Direktsaft
- Fruchtgehalt
- 1 l Pfandfalsche
- e - Zeichen
Rückseite:
- Marle veski
- Sortenzusatz s.o.
-Verkehrsbezeichnung
- Zutaten
- Nährwerttabelle je 100ml
- Lagerungshinweis
- 1l Pfandflasche
- Inverkehrbringeradresse
- Mindestens haltbar bis
ggf. eine Sortendifferenzierung über die Farben.
Die Glasflaschen sind klar.

```html
<!DOCTYPE html>
<html lang="de">
<head>
<meta charset="utf-8">
<title>veski Kirsche – Etiketten</title>
<link rel="stylesheet" href="https://fonts.googleapis.com/css2?family=Barlow:wght@300;400;600;700&display=swap">
<style>
  :root {
    --bg: #ece0cf;
    --wine: #861b1c;
    --label-white: #ffffff;
    --ink: #111111;
    --splash-light: #f3a9b2;
    --splash-mid: #e06676;
    --cherry-deep: #7d1420;
    --leaf: #6f9b55;
  }
  * { margin: 0; padding: 0; box-sizing: border-box; }
  html, body { width: 1004px; height: 1200px; overflow: hidden; }
  body {
    background: var(--bg);
    font-family: "Barlow", Arial, sans-serif;
    position: relative;
  }

  /* ---------- Front body label ---------- */
  .body-label {
    position: absolute;
    left: 23px; top: 352px;
    width: 496px; height: 496px;
    background: var(--label-white);
    overflow: hidden;
  }
  .body-label .band-top {
    position: absolute; left: 0; top: 0; width: 100%; height: 16px;
    background: var(--wine);
  }
  .body-label .splash-corner {
    position: absolute; left: 0; top: 16px; width: 170px; height: 160px;
    background: radial-gradient(ellipse at 35% 35%, var(--splash-mid) 0%, var(--splash-light) 45%, rgba(255,255,255,0) 72%);
    opacity: .8;
  }
  .body-label .fruit-art {
    position: absolute; left: 217px; top: 136px; width: 279px; height: 297px;
    background:
      radial-gradient(circle at 45% 68%, var(--cherry-deep) 0%, #b3293a 26%, var(--splash-mid) 48%, rgba(243,169,178,0.55) 66%, rgba(255,255,255,0) 80%),
      linear-gradient(160deg, rgba(255,255,255,0) 55%, rgba(111,155,85,0.35) 100%);
  }
  .body-label .brand {
    position: absolute; left: 68px; top: 26px;
    font-weight: 300; font-size: 112px; line-height: 1;
    color: var(--wine); letter-spacing: -1px;
  }
  .body-label .variety {
    position: absolute; left: 109px; top: 166px;
    font-weight: 700; font-size: 33px; letter-spacing: 4px; color: var(--ink);
  }
  .body-label .descriptor {
    position: absolute; left: 109px; top: 204px;
    font-weight: 400; font-size: 13px; line-height: 17px; letter-spacing: 1px; color: var(--ink);
  }
  .body-label .fruit-content {
    position: absolute; left: 29px; top: 341px;
    font-weight: 700; font-size: 13px; line-height: 16px; letter-spacing: 1.4px; color: var(--wine);
  }
  .body-label .volume {
    position: absolute; left: 29px; top: 380px;
    font-weight: 300; font-size: 24px; line-height: 1; color: var(--ink);
  }
  .body-label .volume .e-mark { font-weight: 700; font-size: 26px; margin-right: 3px; }
  .body-label .deposit {
    position: absolute; left: 31px; top: 409px;
    font-size: 9px; letter-spacing: 1.3px; color: var(--ink);
  }
  .body-label .band-bottom {
    position: absolute; left: 0; top: 433px; width: 100%; height: 34px;
    background: var(--wine);
  }
  .body-label .range-name {
    position: absolute; left: 0; width: 100%; top: 7px;
    text-align: center; font-weight: 600; font-size: 17px; letter-spacing: 1px;
    color: var(--label-white);
  }
  .body-label .batch-code {
    position: absolute; right: 26px; top: 13px;
    font-size: 8px; letter-spacing: 1px; color: #e7c9c9;
  }
  .body-label .stripe-bottom {
    position: absolute; left: 0; top: 480px; width: 100%; height: 16px;
    background: var(--wine);
  }

  /* ---------- Neck label ---------- */
  .neck-label {
    position: absolute;
    left: 542px; top: 410px;
    width: 439px; height: 381px;
  }
  .neck-label svg { position: absolute; left: 0; top: 0; }
  .neck-label .fruit-art {
    position: absolute; left: 126px; top: 54px; width: 186px; height: 112px;
    background: radial-gradient(ellipse at 55% 62%, var(--cherry-deep) 0%, #b3293a 25%, var(--splash-mid) 45%, rgba(243,169,178,0.5) 62%, rgba(255,255,255,0) 78%);
  }
  .neck-label .brand {
    position: absolute; left: 0; width: 100%; top: 158px; text-align: center;
    font-weight: 300; font-size: 96px; line-height: 1; color: var(--wine);
  }
  .neck-label .variety {
    position: absolute; left: 0; width: 100%; top: 244px; text-align: center;
    font-weight: 700; font-size: 29px; letter-spacing: 4px; color: var(--ink);
  }
  .neck-label .descriptor {
    position: absolute; left: 0; width: 100%; top: 276px; text-align: center;
    font-size: 12px; line-height: 16px; letter-spacing: 1px; color: var(--ink);
  }
  .neck-label .fruit-content {
    position: absolute; left: 0; width: 100%; top: 315px; text-align: center;
    font-weight: 700; font-size: 13px; letter-spacing: 1px; color: var(--label-white);
  }
  .neck-label .batch-code {
    position: absolute; left: 80px; top: 80px;
    font-size: 8px; letter-spacing: 1px; color: var(--ink);
    transform: rotate(-90deg); transform-origin: left top;
  }
</style>
</head>
<body>

  <section class="body-label" aria-label="Front-Bauchetikett veski Kirsche">
    <div class="band-top"></div>
    <div class="splash-corner" role="img" aria-label="Aquarell-Spritzer in Kirschrot"></div>
    <div class="fruit-art" role="img" aria-label="Aquarell-Illustration: drei Sauerkirschen am Stiel mit Blatt und rotem Saftspritzer"></div>
    <div class="brand">veski</div>
    <div class="variety">KIRSCHE</div>
    <div class="descriptor">Sauerkirsch-Nektar<br>aus Sauerkirschsaftkonzentrat</div>
    <div class="fruit-content">FRUCHTGEHALT:<br>MINDESTENS 50%</div>
    <div class="volume"><span class="e-mark">e</span>1,0l</div>
    <div class="deposit">PFANDFLASCHE</div>
    <div class="band-bottom">
      <div class="range-name">veski SÄFTE</div>
      <div class="batch-code">11234V&nbsp;&nbsp;H11</div>
    </div>
    <div class="stripe-bottom"></div>
  </section>

  <section class="neck-label" aria-label="Front-Halsetikett veski Kirsche">
    <svg width="439" height="381" viewBox="0 0 767 665">
      <defs>
        <clipPath id="neck-inner">
          <path d="M78,48 Q383,105 688,48 Q705,44 708,62 L735,515 Q738,545 705,560 Q383,660 62,560 Q30,545 32,515 L58,62 Q61,44 78,48 Z"/>
        </clipPath>
      </defs>
      <path fill="var(--wine)" d="M62,12 Q383,72 704,12 Q735,6 742,40 L766,520 Q770,565 730,585 Q383,712 37,585 Q-3,565 1,520 L25,40 Q32,6 62,12 Z"/>
      <path fill="var(--label-white)" d="M78,48 Q383,105 688,48 Q705,44 708,62 L735,515 Q738,545 705,560 Q383,660 62,560 Q30,545 32,515 L58,62 Q61,44 78,48 Z"/>
      <rect x="0" y="540" width="767" height="48" fill="var(--wine)" clip-path="url(#neck-inner)"/>
    </svg>
    <div class="fruit-art" role="img" aria-label="Aquarell-Illustration: zwei Kirschen mit Blatt und rotem Saftspritzer"></div>
    <div class="batch-code">11234V&nbsp;&nbsp;H11</div>
    <div class="brand">veski</div>
    <div class="variety">KIRSCHE</div>
    <div class="descriptor">Sauerkirsch-Nektar<br>aus Sauerkirschsaftkonzentrat</div>
    <div class="fruit-content">Fruchtgehalt: mindestens 50%</div>
  </section>

</body>
</html>
```